New Management Consultant needs a Stationery Design

We are in need of a full image & identity design for a management consultancy named Varuno Solutions.

Varuno Solutions is a management consulting business focusing on the mining and resources sector that specialises in Supply Chain, Integrated Planning, Operational Leadership, Health & Safety, Logistics, Accommodation & Facilities Management and Business Process Improvement.

Excerpt from WorkNodd Profile:

"A Senior Process Improvement Professional, specialising in logistics, with over 20 years experience with a blue chip resource company (iron ore and diamonds). Expertise in operational leadership, logistics, business process improvement and financial management. Outstanding history of successful achievements, especially in mine scheduling system design (patents certified), cost reduction and business improvement.

Senior management role key strengths include exceptional complex problem solving, contract/contractor management, logistics scheduling and the ability to implement process improvement and optimization at all stages in the business cycle."

The overall feel should be "Efficient, Dynamic, Experienced".

The design should communicate Professional, Efficient & Creative (Think outside the box)

We require:

Business Logo
Business Card
E-Business Card (send by email and Mac Contacts)
A4 Letterhead
A4 Follower page
Invoice Template (see attached)
Presentation Template (see attached - colour scheme to be used in all the design components)

ALSO NEED recommendation for standard Font ( to be compatable with MS Word) for corporate communication.

Must Have:
- LETTERHEAD must have the following details on them

Varuno Solutions
PO Box 814, Lurnea WA 6170
M 0428 315 604
E desmond.varuno@tealmail.com

BUSINESS CARD should have the following details

Desmond Kitto
Director
Varuno Solutions
PO Box 814, Lurnea WA 6170
M 0428 315 604

Industry/Entity Type

Management Consulting

```html
<!DOCTYPE html>
<html lang="en">
<head>
<meta charset="utf-8">
<title>Varuno Solutions — Stationery Set</title>
<link rel="stylesheet" href="https://fonts.googleapis.com/css2?family=Questrial&family=Open+Sans:wght@400;600;700&display=swap">
<style>
  :root {
    --navy: #0b4a85;
    --blue: #1c9ddd;
    --sky: #8fd1ef;
    --row: #cbe9f8;
    --ink: #4a4a4a;
    --mute: #8a8a8a;
    --ghost: #ececec;
    --paper: #ffffff;
    --stage: #e4e4e4;
  }
  * { box-sizing: border-box; margin: 0; padding: 0; }
  html, body { width: 1200px; height: 795px; overflow: hidden; }
  body {
    background: var(--stage);
    font-family: "Open Sans", Arial, sans-serif;
    color: var(--ink);
    position: relative;
  }
  .sheet {
    position: absolute;
    background: var(--paper);
    box-shadow: 0 2px 6px rgba(0,0,0,.12);
    overflow: hidden;
  }
  .brand-name { font-family: "Questrial", Arial, sans-serif; font-weight: 400; white-space: nowrap; }
  .brand-dot { border-radius: 50%; background: var(--blue); flex: none; }
  .brand { display: flex; align-items: center; }

  /* Logo panel */
  .logo-panel { left: 40px; top: 40px; width: 290px; height: 170px;
    display: flex; flex-direction: column; align-items: center; justify-content: center; gap: 12px; }
  .logo-panel .brand-dot { width: 78px; height: 78px; background: linear-gradient(180deg, var(--blue), var(--navy)); }
  .logo-panel .brand-name { font-size: 25px; color: #555; }

  /* Business card back */
  .card-back { left: 40px; top: 235px; width: 290px; height: 170px; background: var(--navy);
    display: flex; align-items: center; justify-content: center; gap: 14px; }
  .card-back .brand-dot { width: 60px; height: 60px; background: #fff; }
  .card-back .brand-name { font-size: 24px; color: #fff; }

  /* Business card front */
  .card-front { left: 40px; top: 430px; width: 290px; height: 170px; }
  .card-front .swoosh { position: absolute; inset: 0; }
  .card-front .seal { position: absolute; left: 22px; top: 66px; width: 92px; height: 92px; border-radius: 50%;
    background: linear-gradient(180deg, var(--blue), var(--navy)); }
  .card-front .person { position: absolute; left: 138px; top: 58px; }
  .card-front .person-name { font-size: 14px; font-weight: 700; color: var(--navy); }
  .card-front .person-role { font-size: 8px; color: var(--mute); }
  .card-front .contact { position: absolute; left: 138px; top: 100px; list-style: none; font-size: 8px; line-height: 14px; color: #555; }
  .contact-icon { display: inline-block; width: 9px; height: 9px; background: var(--navy); margin-right: 5px; vertical-align: -1px; }

  /* Letterhead */
  .letterhead { left: 365px; top: 40px; width: 385px; height: 545px; }
  .letterhead .swoosh { position: absolute; left: 0; top: 0; }
  .letterhead .brand { position: absolute; right: 26px; top: 26px; gap: 6px; }
  .letterhead .brand-dot { width: 20px; height: 20px; }
  .letterhead .brand-name { font-size: 13px; color: #555; }
  .ghost-disc { position: absolute; border-radius: 50%; background: var(--ghost); }
  .letterhead .ghost-disc { right: 20px; bottom: 50px; width: 190px; height: 190px; }
  .letterhead .footer-line { position: absolute; left: 0; right: 0; bottom: 14px; height: 4px; background: var(--navy); }
  .letterhead .footer-text { position: absolute; left: 0; right: 0; bottom: 24px; text-align: center; font-size: 7px; color: var(--navy); font-weight: 600; }

  /* Invoice */
  .invoice { left: 775px; top: 40px; width: 385px; height: 545px; padding: 22px 22px 0; }
  .invoice .head { display: flex; justify-content: space-between; }
  .invoice .brand { gap: 6px; margin-top: 44px; }
  .invoice .brand-dot { width: 22px; height: 22px; }
  .invoice .brand-name { font-size: 13px; color: #555; }
  .invoice .doc-title { text-align: right; }
  .invoice .doc-title h1 { font-family: "Questrial", Arial, sans-serif; font-size: 22px; font-weight: 400; color: var(--mute); letter-spacing: 1px; }
  .invoice .doc-title p { font-size: 6px; line-height: 9px; color: #666; }
  .invoice .bill-to { margin-top: 10px; font-size: 7px; line-height: 10px; color: #444; }
  .invoice .bill-to strong { display: block; color: var(--navy); font-size: 8px; }
  .invoice .meta { position: absolute; right: 22px; top: 98px; font-size: 6px; color: #666; text-align: right; line-height: 9px; }
  .items { width: 100%; border-collapse: collapse; margin-top: 10px; font-size: 6px; }
  .items th { background: var(--sky); color: var(--navy); font-weight: 600; text-align: left; padding: 4px 5px; text-transform: uppercase; }
  .items td { height: 17px; border-left: 1px solid #fff; }
  .items tr:nth-child(odd) td { background: var(--row); }
  .items col.desc { width: 46%; }
  .totals { margin-left: auto; width: 44%; border-collapse: collapse; font-size: 6px; margin-top: 6px; }
  .totals th { text-align: left; font-weight: 600; color: var(--navy); padding: 3px 5px; background: var(--row); text-transform: uppercase; }
  .totals td { width: 45%; background: var(--sky); border-left: 1px solid #fff; }
  .totals tr.due th { font-weight: 700; }
  .invoice .sign { position: absolute; left: 22px; right: 22px; bottom: 40px; display: flex; justify-content: space-between;
    font-size: 7px; font-weight: 700; color: #333; z-index: 1; }
  .invoice .sign span { border-top: 1px dotted #999; padding-top: 3px; width: 30%; }
  .invoice .ghost-disc { left: 40px; bottom: 20px; width: 110px; height: 110px; }
</style>
</head>
<body>

  <section class="sheet logo-panel" aria-label="Primary logo">
    <div class="brand-dot"></div>
    <span class="brand-name">Varuno Solutions</span>
  </section>

  <section class="sheet card-back" aria-label="Business card, reverse">
    <div class="brand-dot"></div>
    <span class="brand-name">Varuno Solutions</span>
  </section>

  <section class="sheet card-front" aria-label="Business card, front">
    <svg class="swoosh" width="290" height="170" viewBox="0 0 290 170" aria-hidden="true">
      <path d="M0 0 H290 V4 C190 10 90 40 0 95 Z" fill="var(--navy)"/>
      <path d="M0 95 C90 40 190 10 290 4 V8 C190 18 100 52 0 112 Z" fill="var(--blue)"/>
    </svg>
    <div class="seal"></div>
    <div class="person">
      <div class="person-name">Desmond Kitto</div>
      <div class="person-role">Director</div>
    </div>
    <ul class="contact">
      <li><span class="contact-icon"></span>0428 315 604</li>
      <li><span class="contact-icon"></span>desmond.varuno@tealmail.com</li>
      <li><span class="contact-icon"></span>PO Box 814, Lurnea WA 6170</li>
    </ul>
  </section>

  <section class="sheet letterhead" aria-label="A4 letterhead">
    <svg class="swoosh" width="385" height="200" viewBox="0 0 385 200" aria-hidden="true">
      <path d="M0 0 H60 C40 50 25 120 0 190 Z" fill="var(--navy)"/>
      <path d="M0 190 C25 120 40 50 60 0 H68 C46 60 30 130 0 200 Z" fill="var(--blue)"/>
    </svg>
    <div class="brand">
      <div class="brand-dot"></div>
      <span class="brand-name">Varuno Solutions</span>
    </div>
    <div class="ghost-disc"></div>
    <p class="footer-text">M 0428 315 604 &nbsp;|&nbsp; E desmond.varuno@tealmail.com &nbsp;|&nbsp; PO Box 814, Lurnea WA 6170</p>
    <div class="footer-line"></div>
  </section>

  <section class="sheet invoice" aria-label="Invoice template">
    <div class="head">
      <div>
        <div class="brand">
          <div class="brand-dot"></div>
          <span class="brand-name">Varuno Solutions</span>
        </div>
        <div class="bill-to">
          <strong>Invoice Slip To</strong>
          Harlan Preece<br>
          14 Carrow Street, Bayfield<br>
          Perth, WA 6000
        </div>
      </div>
      <div class="doc-title">
        <h1>INVOICE</h1>
        <p>M 0428 315 604</p>
        <p>desmond.varuno@tealmail.com</p>
        <p>PO Box 814, Lurnea WA 6170</p>
      </div>
    </div>
    <div class="meta">No: 0001<br>Date: 01/01</div>

    <table class="items">
      <colgroup><col class="desc"><col><col><col></colgroup>
      <thead><tr><th>Description</th><th>Quantity</th><th>Unit Price</th><th>Amount</th></tr></thead>
      <tbody>
        <tr><td></td><td></td><td></td><td></td></tr>
        <tr><td></td><td></td><td></td><td></td></tr>
        <tr><td></td><td></td><td></td><td></td></tr>
        <tr><td></td><td></td><td></td><td></td></tr>
        <tr><td></td><td></td><td></td><td></td></tr>
        <tr><td></td><td></td><td></td><td></td></tr>
        <tr><td></td><td></td><td></td><td></td></tr>
        <tr><td></td><td></td><td></td><td></td></tr>
        <tr><td></td><td></td><td></td><td></td></tr>
        <tr><td></td><td></td><td></td><td></td></tr>
      </tbody>
    </table>

    <table class="totals">
      <tr><th>Subtotal</th><td></td></tr>
      <tr><th>Tax Rate</th><td></td></tr>
      <tr><th>Tax</th><td></td></tr>
      <tr class="due"><th>Amount Due</th><td></td></tr>
    </table>

    <div class="ghost-disc"></div>
    <div class="sign"><span>Notes:</span><span>Signature</span><span>Date</span></div>
  </section>

</body>
</html>
```